Graphic design for "How It Works" for VelmoraStyles.com*

VelmoraStyles.com website is for selling custom designer outfits for women and girls in all countries, customers can choose existing designs on this website and customize to their measurements. Customers can also provide their own designs and measurements and our expert designers and tailors get the outfit stitched and delivered to the customer.

We wanted to explain how this entire process works in 4 steps in the form of graphic design with little heading and text describing each step.

Step 1: Select Dress
Its time to choose the beauty you want to adorn yourself with. We have a wide collection of premium dresses, colours and accessories. There is something for everyone! All you need to do is pick. If you can’t find what you are looking for then you can share a picture of what you want, we will get it done whatever you want.

Step 2: Customization
Everyone is different; hence we realise the need for customization of the design and size. Here you select exactly how you want your dress to be. From sleeves to cuts, everything will be done as per your wish. Enter your measurements, lo and behold! You’re done. Leave your comments for even more customization.

Step 3: Designer Consultation
We as a user-friendly brand, aspire to provide the best of services to our clients. Our expert lady designers will help you for everything right from selecting of fabric to design of dress to necessary accessories. Our designers are just a call away!

Step 4: Stitch and Deliver
After you have placed your order, we confirm and verify the details. The boutique completes your order, sends it to us and we deliver it to your doorstep. We also have a team of designers in-house to cater to your premium dressing needs.

```html
<!DOCTYPE html>
<html lang="en">
<head>
<meta charset="utf-8">
<title>How it works – VelmoraStyles.com</title>
<link rel="stylesheet" href="https://fonts.googleapis.com/css2?family=Open+Sans:wght@600&family=Oswald:wght@500&family=Source+Sans+3:wght@400&display=swap">
<style>
  :root {
    --title-pink: #d8336b;
    --step-red: #ef4e37;
    --step-teal: #42919a;
    --step-blue: #1f74bd;
    --step-purple: #8b3a79;
    --fill-cream: #fdfbef;
    --fill-mint: #eef5f2;
    --fill-sky: #eef6fc;
    --fill-lavender: #f4eff6;
    --text-dark: #2b2b2b;
    --icon-dark: #1e1e1e;
    --page: #ffffff;
  }
  * { margin: 0; padding: 0; box-sizing: border-box; }
  html, body { width: 1200px; height: 370px; overflow: hidden; background: var(--page); }
  .canvas { position: relative; width: 1200px; height: 370px; font-family: "Source Sans 3", Arial, sans-serif; color: var(--text-dark); }
  .page-title {
    position: absolute; top: 10px; left: 0; width: 1200px;
    text-align: center; font-family: "Open Sans", Arial, sans-serif; font-size: 40px; font-weight: 600;
    color: var(--title-pink); letter-spacing: -0.5px; line-height: 50px;
  }
  .frames { position: absolute; top: 0; left: 0; }
  .step-heading {
    position: absolute; top: 174px; width: 260px; margin-left: -130px;
    text-align: center; font-family: "Oswald", "Arial Narrow", sans-serif;
    font-weight: 500; font-size: 22px; line-height: 28px; color: #fff; letter-spacing: 0.4px;
  }
  .step-text {
    position: absolute; width: 240px; margin-left: -120px;
    text-align: center; white-space: nowrap;
    font-size: 11.6px; line-height: 14.5px;
  }
  .step-text--loose { font-size: 12.6px; line-height: 16px; }
</style>
</head>
<body>
<div class="canvas">
  <h1 class="page-title">How it works</h1>

  <svg class="frames" width="1200" height="370" viewBox="0 0 1880 580">
    <defs>
      <filter id="hex-shadow" x="-10%" y="-10%" width="125%" height="125%">
        <feDropShadow dx="6" dy="7" stdDeviation="4" flood-color="#000" flood-opacity="0.28"/>
      </filter>
      <polygon id="hex-fill" points="170,140 405,140 522,345 405,548 170,548 38,345"/>
      <polyline id="hex-frame" points="447,180 413,123 150,123 18,345 150,565 413,565 447,505" fill="none" stroke-width="3"/>
      <polygon id="hex-band" points="86,270 470,270 497,318 60,318"/>
    </defs>

    <g class="step step--select">
      <use href="#hex-frame" stroke="var(--step-red)"/>
      <circle cx="453" cy="191" r="8" fill="#fff" stroke="var(--step-red)" stroke-width="3"/>
      <circle cx="453" cy="495" r="8" fill="#fff" stroke="var(--step-red)" stroke-width="3"/>
      <use href="#hex-fill" fill="var(--fill-cream)" filter="url(#hex-shadow)"/>
      <use href="#hex-band" fill="var(--step-red)"/>
      <rect x="210" y="150" width="115" height="105" rx="10" fill="var(--icon-dark)" opacity="0.85" role="img" aria-label="Dress icon with checklist"/>
    </g>

    <g class="step step--custom" transform="translate(442 0)">
      <use href="#hex-frame" stroke="var(--step-teal)"/>
      <circle cx="453" cy="191" r="8" fill="#fff" stroke="var(--step-teal)" stroke-width="3"/>
      <circle cx="453" cy="495" r="8" fill="#fff" stroke="var(--step-teal)" stroke-width="3"/>
      <use href="#hex-fill" fill="var(--fill-mint)" filter="url(#hex-shadow)"/>
      <use href="#hex-band" fill="var(--step-teal)"/>
      <rect x="185" y="172" width="165" height="62" rx="10" fill="var(--icon-dark)" opacity="0.85" role="img" aria-label="Scissors icon"/>
    </g>

    <g class="step step--consult" transform="translate(884 0)">
      <use href="#hex-frame" stroke="var(--step-blue)"/>
      <circle cx="447" cy="191" r="8" fill="#fff" stroke="var(--step-blue)" stroke-width="3"/>
      <circle cx="447" cy="495" r="8" fill="#fff" stroke="var(--step-blue)" stroke-width="3"/>
      <use href="#hex-fill" fill="var(--fill-sky)" filter="url(#hex-shadow)"/>
      <use href="#hex-band" fill="var(--step-blue)"/>
      <rect x="205" y="155" width="115" height="95" rx="40" fill="var(--icon-dark)" opacity="0.85" role="img" aria-label="Support headset icon"/>
    </g>

    <g class="step step--deliver" transform="translate(1326 0)">
      <polyline points="140,123 413,123 535,345 413,565 140,565 50,420" fill="none" stroke="var(--step-purple)" stroke-width="3"/>
      <use href="#hex-fill" fill="var(--fill-lavender)" filter="url(#hex-shadow)"/>
      <use href="#hex-band" fill="var(--step-purple)"/>
      <rect x="180" y="155" width="175" height="95" rx="10" fill="var(--icon-dark)" opacity="0.85" role="img" aria-label="Sewing machine and parcel icon"/>
    </g>
  </svg>

  <h2 class="step-heading" style="left:177px">Select Dress</h2>
  <h2 class="step-heading" style="left:455px">Customization</h2>
  <h2 class="step-heading" style="left:742px">Designer Consultation</h2>
  <h2 class="step-heading" style="left:1021px">Stitch and Deliver</h2>

  <p class="step-text" style="left:177px; top:206px">Its time to choose the beauty you want to<br>adorn yourself with. We have a wide<br>collection of premium dresses, colours and<br>accessories. There is something for<br>everyone! All you need to do is pick. If you<br>can’t find what you are looking for then<br>you can share a picture of what<br>you want, we will get it done<br>whatever you want.</p>

  <p class="step-text" style="left:463px; top:206px">Everyone is different; hence we realise<br>the need for customization of the design<br>and size. Here you select exactly how<br>you want your dress to be. From sleeves<br>to cuts, everything will be done as per<br>your wish. Enter your measurements, lo<br>and behold! You’re done.<br>Leave your comments for even<br>more customization.</p>

  <p class="step-text step-text--loose" style="left:738px; top:207px">We as a user-friendly brand, aspire<br>to provide the best of services to our<br>clients. Our expert lady designers<br>will help you for everything right<br>from selecting of fabric to design of<br>dress to necessary accessories. Our<br>designers are just a call away!</p>

  <p class="step-text step-text--loose" style="left:1021px; top:209px">After you have placed your order, we<br>confirm and verify the details. The<br>boutique completes your order, sends<br>it to us and we deliver it to your<br>doorstep. We also have a team of<br>designers in-house to cater to your<br>premium dressing needs.</p>
</div>
</body>
</html>
```